Roofing web site brvt roofing

Look at some of our competitors web page we like something similar with NYC roofing
https://www.dellowtopcoat.example/
Maybe a skyline picture of nyc at the home page with a picture of flat roofing installation

Target Market(s)

Commercial and residential flat roofs

Industry/Entity Type

Flat Roofing industry

Coding

Coded - Design and coding required

Number of Pages Required

2 page

Font styles to use
Decorative
Script

Colors

Designer to choose colors to be used in the design.

Requirements
Must have
• At BRVT Roofing, we are a trusted and reputable roofing company specializing in new construction flat roof installation and repair. With years of experience in the industry, we take pride in providing exceptional roofing solutions to our valued clients. Our team of highly skilled and dedicated roofing professionals understands the unique challenges and requirements of new construction projects. We work closely with builders, contractors, and architects to design and install flat roofs that meet the specific needs of each project. From commercial buildings to residential complexes, we have the expertise to deliver reliable and durable roofing solutions. When it comes to flat roof repairs, we are your go-to experts. Our experienced technicians conduct thorough inspections to identify the root cause of any issues your roof may be experiencing. We utilize the latest industry techniques and high-quality materials to efficiently repair your flat roof, ensuring its integrity and longevity. At BRVT Roofing, we prioritize customer satisfaction above all else. We believe in building strong relationships with our clients by providing exceptional craftsmanship and outstanding customer service. Our team is dedicated to delivering projects on time, within budget, and to the highest standards of quality. We understand that a well-maintained roof is essential for protecting your property and ensuring the safety of its occupants. That's why we use only the best materials and employ skilled professionals who are trained in the latest roofing practices. Our commitment to excellence is evident in every project we undertake. As a fully licensed and insured roofing company, we prioritize safety and adhere to industry regulations and best practices. We take every precaution to create a safe working environment for our team and minimize any disruptions to your daily routine. When you choose BRVT Roofing, you can trust that you are working with a reliable and reputable company that will deliver exceptional results. We are committed to exceeding your expectations and providing you with a roof that is built to last. Contact us today for all your new construction flat roof installation and repair needs.
Nice to have
• NYC skyline background with commercial roofing pictures of torching roofing

```html
<!DOCTYPE html>
<html lang="en">
<head>
<meta charset="utf-8">
<title>BRVT Roofing</title>
<link href="https://fonts.googleapis.com/css2?family=Cinzel:wght@400;600;700&family=Poppins:wght@400;500&display=swap" rel="stylesheet">
<style>
:root{
  --orange:#f26a21;
  --orange-light:#fb8a2e;
  --dark:#3a3a3a;
  --ink:#1d1d1d;
  --footer:#2b2b2b;
  --footer-bottom:#222;
  --text:#333;
  --muted:#555;
  --light:#f4f4f4;
  --beige:#e8dfcf;
  --white:#fff;
}
*{margin:0;padding:0;box-sizing:border-box}
html,body{width:1200px;height:4423px;overflow:hidden}
body{position:relative;font-family:'Poppins',sans-serif;color:var(--text);background:var(--white)}
.abs{position:absolute}
.serif{font-family:'Cinzel',serif}
.btn{position:absolute;display:flex;align-items:center;justify-content:center;font-family:'Cinzel',serif;font-weight:600;color:var(--white);letter-spacing:1px;font-size:16px;text-decoration:none}
.btn-orange{background:var(--orange)}
.btn-dark{background:var(--ink)}
/* header */
.logo{left:74px;top:24px;width:136px;height:70px;border:2px solid #666;font-family:'Cinzel',serif;font-size:20px;line-height:24px;color:#333;padding:8px 14px}
.phone{left:532px;top:33px;display:flex;align-items:center;gap:14px;font-size:32px;font-family:'Cinzel',serif;color:#222}
.phone-icon{width:50px;height:50px;border:2px solid var(--orange);border-radius:50%;display:flex;align-items:center;justify-content:center}
.nav{left:0;top:117px;width:1200px;height:67px;background:var(--dark)}
.nav a{position:absolute;top:18px;font-family:'Cinzel',serif;font-size:24px;color:var(--white);text-decoration:none;letter-spacing:1px}
/* hero */
.hero{left:0;top:184px;width:1200px;height:635px;background:linear-gradient(90deg,#6aaee6 0%,#7cb7e8 40%,#8aa9c4 60%,#4a4e56 85%,#3d3f44 100%)}
.hero-title{left:74px;top:370px;font-size:58px;color:var(--ink);font-weight:600}
.hero-text{left:74px;top:448px;font-size:21px;line-height:31px;color:#111}
.dots{left:563px;top:771px;display:flex;gap:10px}
.dots span{width:10px;height:10px;border-radius:50%;background:#222}
.dots span:first-child{background:var(--orange)}
/* welcome */
.frame-orange{left:60px;top:896px;width:190px;height:143px;background:var(--orange)}
.frame-dark{left:60px;top:1217px;width:190px;height:141px;background:var(--ink)}
.welcome-photo{left:72px;top:910px;width:515px;height:434px;border-radius:0 30px 0 30px;background:linear-gradient(160deg,#7a8690,#41505d 55%,#24303a)}
.welcome-h{left:615px;top:958px;font-size:48px;line-height:54px;font-weight:600;color:var(--ink)}
.welcome-h span{color:var(--orange)}
.welcome-p{left:615px;top:1083px;width:500px;font-size:15.5px;line-height:31.5px;color:#333}
/* services */
.svc-band{left:0;top:1454px;width:1200px;height:284px;background:linear-gradient(180deg,#f0662a,#f27a2a 60%,#f58b35)}
.svc-title{left:0;top:1500px;width:1200px;text-align:center;font-size:56px;color:var(--white);font-weight:600}
.card{width:329px;height:279px;top:1598px;border:5px solid var(--white);border-radius:16px;box-shadow:0 2px 8px rgba(0,0,0,.25)}
.card-title{width:329px;text-align:center;top:1905px;font-size:28px;line-height:34px;color:var(--orange);font-weight:600}
.card-text{width:329px;text-align:center;top:1983px;font-size:15px;line-height:29px;color:#444}
/* expert */
.expert-line{left:0;width:1200px;height:18px;background:var(--beige)}
.expert{left:0;top:2259px;width:1200px;height:544px;background:linear-gradient(90deg,#000 0%,#0b0b0b 42%,#3c4450 60%,#6f7884 80%,#9aa3ae 100%)}
.expert-h{left:75px;top:2322px;font-size:52px;line-height:52px;color:var(--white);font-weight:600}
.expert-sub{left:75px;top:2457px;font-size:33px;color:var(--orange);font-weight:600}
.expert-p{left:75px;top:2512px;width:570px;font-size:15.5px;line-height:33px;color:var(--white)}
/* gallery */
.gallery-title{left:0;top:2884px;width:1200px;text-align:center;font-size:52px;color:var(--ink);font-weight:600}
.g{width:340px;height:205px}
/* newsletter */
.news{left:0;top:3580px;width:1200px;height:433px;background:var(--light)}
.news-h{left:0;top:3675px;width:1200px;text-align:center;font-size:38px;line-height:50px;color:var(--ink);font-weight:600;letter-spacing:1px}
.news-p{left:0;top:3797px;width:1200px;text-align:center;font-size:17px;color:#333}
.email{left:290px;top:3851px;width:445px;height:55px;border:2px solid #bbb;background:var(--white);padding:0 14px;display:flex;align-items:center;font-size:13px;color:#333}
/* footer */
.footer{left:0;top:4013px;width:1200px;height:334px;background:var(--footer)}
.f-head{top:4080px;font-size:23px;color:var(--white);font-family:'Cinzel',serif;letter-spacing:1px}
.f-list{top:4129px;font-size:15px;line-height:41.5px;color:var(--white);list-style:none}
.contact-row{display:flex;align-items:center;gap:18px}
.socials{left:884px;top:4236px;display:flex;gap:18px}
.socials span{width:24px;height:24px;border-radius:50%;background:var(--white)}
.bottom{left:0;top:4347px;width:1200px;height:76px;background:var(--footer-bottom);color:var(--white);font-size:14px;display:flex;align-items:center;justify-content:center}
</style>
</head>
<body>

<header>
  <div class="abs logo">BRVT<br>Roofing</div>
  <div class="abs phone">
    <span class="phone-icon"><svg width="24" height="24" viewBox="0 0 24 24"><path d="M6.6 10.8c1.4 2.8 3.8 5.2 6.6 6.6l2.2-2.2c.3-.3.7-.4 1-.2 1.1.4 2.3.6 3.6.6.6 0 1 .4 1 1V20c0 .6-.4 1-1 1C10.6 21 3 13.4 3 4c0-.6.4-1 1-1h3.5c.6 0 1 .4 1 1 0 1.3.2 2.5.6 3.6.1.3 0 .7-.2 1L6.6 10.8z" fill="#f26a21"/></svg></span>
    555-014-2290
  </div>
  <a class="btn btn-orange" style="left:855px;top:29px;width:271px;height:60px;font-size:21px">GET A FREE QUOTE</a>
  <nav class="abs nav">
    <a style="left:146px">Home</a>
    <a style="left:295px">About</a>
    <a style="left:463px">Services</a>
    <a style="left:650px">Photo Gallery</a>
    <a style="left:930px">Contact</a>
  </nav>
</header>

<section>
  <div class="abs hero" role="img" aria-label="Roofer torching down membrane on a flat roof with the city skyline behind"></div>
  <h1 class="abs serif hero-title">BRVT Roofing</h1>
  <p class="abs hero-text">Professional &amp; Affordable Roofing Services.<br>Call Today For a Free Quote!&nbsp; Storm damage,<br>roof installation, roof repair.</p>
  <a class="btn btn-orange" style="left:74px;top:561px;width:168px;height:55px;font-size:19px">Book Now</a>
  <div class="abs dots"><span></span><span></span><span></span><span></span></div>
</section>

<section>
  <div class="abs frame-orange"></div>
  <div class="abs frame-dark"></div>
  <div class="abs welcome-photo" role="img" aria-label="Roofer laying torch-on membrane across a flat roof"></div>
  <h2 class="abs serif welcome-h">Welcome to<br><span>BRVT Roofing</span></h2>
  <p class="abs welcome-p">Dorian brought together the best in the business to create his dream. Though he takes pride in all aspects of roofing, working and living on the coast has lead to a passion for quick, efficient, and transparent repairs to storm damaged homes.</p>
  <a class="btn btn-orange" style="left:615px;top:1234px;width:166px;height:55px">Learn More</a>
</section>

<section>
  <div class="abs svc-band" role="img" aria-label="Orange tinted city skyline"></div>
  <h2 class="abs serif svc-title">Our Services</h2>
  <div class="abs card" style="left:74px;background:linear-gradient(150deg,#d9dfe2,#9aa4aa)" role="img" aria-label="Roofer repairing a roof leak"></div>
  <div class="abs card" style="left:434px;background:linear-gradient(150deg,#e0703a,#b6461f)" role="img" aria-label="Cleaning flashing on a tiled roof"></div>
  <div class="abs card" style="left:795px;background:linear-gradient(180deg,#9fb0c2,#e7e9ea 55%,#cfd3d6)" role="img" aria-label="Worker applying waterproof coating on a flat roof"></div>
  <svg class="abs" style="left:22px;top:1832px" width="28" height="52" viewBox="0 0 28 52"><path d="M25 2L3 26l22 24" fill="none" stroke="#333" stroke-width="3"/></svg>
  <svg class="abs" style="left:1140px;top:1832px" width="28" height="52" viewBox="0 0 28 52"><path d="M3 2l22 24L3 50" fill="none" stroke="#333" stroke-width="3"/></svg>
  <h3 class="abs serif card-title" style="left:74px">Roof Leak<br>Repairs</h3>
  <h3 class="abs serif card-title" style="left:434px">Flashing<br>Services</h3>
  <h3 class="abs serif card-title" style="left:795px">Waterproofing<br>Experts</h3>
  <p class="abs card-text" style="left:74px">Sed ut perspiciatis unde omnis iste natus error sit&nbsp; voluptatem accusantium doloremque laudantium.</p>
  <p class="abs card-text" style="left:434px">Sed ut perspiciatis unde omnis iste natus error sit&nbsp; voluptatem accusantium doloremque laudantium.</p>
  <p class="abs card-text" style="left:795px">Sed ut perspiciatis unde omnis iste natus error sit&nbsp; voluptatem accusantium doloremque laudantium.</p>
  <a class="btn btn-dark" style="left:155px;top:2093px;width:168px;height:55px">Learn More</a>
  <a class="btn btn-dark" style="left:516px;top:2093px;width:168px;height:55px">Learn More</a>
  <a class="btn btn-dark" style="left:877px;top:2093px;width:168px;height:55px">Learn More</a>
</section>

<section>
  <div class="abs expert-line" style="top:2241px"></div>
  <div class="abs expert" role="img" aria-label="Roll of roofing membrane being torched onto a flat roof"></div>
  <div class="abs expert-line" style="top:2803px"></div>
  <h2 class="abs serif expert-h">Expert Flat Roof<br>Services</h2>
  <h3 class="abs serif expert-sub">Perfect Installs</h3>
  <p class="abs expert-p">Your roof is your main defense against the elements.<br>Let us walk you through the best options to fit your needs and once you feel comfortable with your choice, we'll handle the complete installation.</p>
  <a class="btn btn-orange" style="left:75px;top:2673px;width:167px;height:55px">Learn More</a>
  <svg class="abs" style="left:263px;top:2686px" width="20" height="34" viewBox="0 0 20 34"><path d="M17 2L3 17l14 15" fill="none" stroke="#fff" stroke-width="3"/></svg>
  <svg class="abs" style="left:309px;top:2686px" width="20" height="34" viewBox="0 0 20 34"><path d="M3 2l14 15L3 32" fill="none" stroke="#fff" stroke-width="3"/></svg>
</section>

<section>
  <h2 class="abs serif gallery-title">Photo Gallery</h2>
  <div class="abs g" style="left:74px;top:2982px;background:linear-gradient(160deg,#7c8993,#3b4b58)" role="img" aria-label="Torch-on roofing installation"></div>
  <div class="abs g" style="left:431px;top:2982px;background:linear-gradient(160deg,#6b6a66,#c08a3b 50%,#5a5955)" role="img" aria-label="Roofer using a nail gun on shingles"></div>
  <div class="abs g" style="left:788px;top:2982px;background:linear-gradient(160deg,#3a3d42,#d9dcdf 60%,#f0f0f0)" role="img" aria-label="Applying white roof coating"></div>
  <div class="abs g" style="left:74px;top:3206px;background:linear-gradient(180deg,#bcd9ef,#8fa5bc 55%,#4d6a8a)" role="img" aria-label="Metal roof under blue sky"></div>
  <div class="abs g" style="left:431px;top:3206px;background:linear-gradient(160deg,#e8eaea,#3e5e44 55%,#8c9190)" role="img" aria-label="Roofer in work trousers torching membrane"></div>
  <div class="abs g" style="left:788px;top:3206px;background:linear-gradient(180deg,#5c6168,#3b3e44 55%,#7a4f35)" role="img" aria-label="Rooftop terrace with outdoor seating"></div>
  <a class="btn btn-dark" style="left:517px;top:3456px;width:166px;height:55px">View All</a>
</section>

<section>
  <div class="abs news"></div>
  <h2 class="abs serif news-h">Flat roof installation roof repair storm<br>damage insurance specialists</h2>
  <p class="abs news-p">Sign up to receive maintenance reminders and hear about our latest projects.</p>
  <div class="abs email">Email Address</div>
  <a class="btn btn-orange" style="left:747px;top:3851px;width:166px;height:55px;font-size:18px">Subscribe</a>
</section>

<footer>
  <div class="abs footer"></div>
  <h4 class="abs f-head" style="left:76px">Site Map</h4>
  <ul class="abs f-list" style="left:76px"><li>Home</li><li>About</li><li>Services</li><li>Photo Gallery</li><li>Contact</li></ul>
  <h4 class="abs f-head" style="left:316px">Services</h4>
  <ul class="abs f-list" style="left:316px"><li>Perfect Installs</li><li>Reliable Upgrades</li><li>Upkeep &amp; Repair</li></ul>
  <h4 class="abs f-head" style="left:579px">Hours</h4>
  <ul class="abs f-list" style="left:579px"><li>Monday - Friday: 8am - 5pm</li><li>Saturday - Sunday: 8am-12</li></ul>
  <h4 class="abs f-head" style="left:883px">Contact Us</h4>
  <ul class="abs f-list" style="left:883px">
    <li class="contact-row"><svg width="14" height="14" viewBox="0 0 24 24"><path d="M6.6 10.8c1.4 2.8 3.8 5.2 6.6 6.6l2.2-2.2c.3-.3.7-.4 1-.2 1.1.4 2.3.6 3.6.6.6 0 1 .4 1 1V20c0 .6-.4 1-1 1C10.6 21 3 13.4 3 4c0-.6.4-1 1-1h3.5c.6 0 1 .4 1 1 0 1.3.2 2.5.6 3.6.1.3 0 .7-.2 1L6.6 10.8z" fill="#f26a21"/></svg>555-014-2290</li>
    <li class="contact-row"><svg width="14" height="12" viewBox="0 0 14 12"><rect width="14" height="12" rx="1" fill="#f26a21"/><path d="M0 1l7 5 7-5" fill="none" stroke="#2b2b2b" stroke-width="1.4"/></svg>hello@brvtroofing.example</li>
  </ul>
  <div class="abs socials" aria-label="Social media links"><span></span><span></span><span></span><span></span><span></span></div>
  <div class="abs bottom">Copyright ©2024 BRVT Roofing. All Rights Reserved.</div>
</footer>

</body>
</html>
```